I dont have a logo yet. My mind in color is navy blue and khaki maybe a tiny bit of yellow but open to ideas. name of the business is Prairie Ridge Builders. Dedicated to all sorts of construction commerical and residential. Im Tomas Verdugo owner of business<br/>Address to business is 287 N. Marbury El Paso Tx 79925 <br/>Phone is 9156820374<br/>Id like round corners i also like the see thru card a little.<br/>Open to trademark quotes

Target Market(s)

Construction

Contact Information for Business Card

PRAIRIE RIDGE BUILDERS LLC

Tomas Verdugo
Director of Operations

Commercial & Residential

9156820374
PRAIRIE.R.BUILDERS@MAILHAVEN.NET

Colors
0355a3
fff3d1

Requirements
Must have
• ROUND CORNERS
• BLUE AND KHAKI AND CLEAR
• LOGO

```html
<!DOCTYPE html>
<html lang="en">
<head>
<meta charset="utf-8">
<title>Prairie Ridge Builders — Business Card</title>
<link rel="stylesheet" href="https://fonts.googleapis.com/css2?family=Lato:wght@400;700;900&display=swap">
<style>
  :root {
    --navy: #111448;
    --navy-deep: #0d1040;
    --khaki: #a88d62;
    --white: #ffffff;
    --divider: #9a9cb4;
    --backdrop: #1b1b1d;
  }
  * { box-sizing: border-box; margin: 0; padding: 0; }
  html, body {
    width: 1200px; height: 900px; overflow: hidden;
    background: var(--backdrop);
    font-family: "Lato", sans-serif;
  }
  .canvas {
    position: relative; width: 1200px; height: 900px;
    display: flex; flex-direction: column; align-items: center; justify-content: center; gap: 60px;
  }
  .card {
    position: relative; width: 630px; height: 360px;
    border-radius: 30px; overflow: hidden;
    box-shadow: 0 10px 30px rgba(0,0,0,0.45);
  }
  .brand { display: flex; align-items: center; gap: 10px; }
  .brand__mark { width: 14px; height: 14px; background: var(--navy); flex: none; }
  .brand__name {
    font-weight: 900; text-transform: uppercase; letter-spacing: 1px; line-height: 1.15;
    color: var(--navy);
  }
  /* Front */
  .card--front { background: var(--white); }
  .card--front .brand { position: absolute; left: 44px; top: 96px; width: 220px; }
  .card--front .brand__name { font-size: 20px; }
  .address {
    position: absolute; left: 44px; bottom: 46px;
    font-size: 16px; color: var(--khaki);
  }
  .divider {
    position: absolute; left: 282px; top: 90px; width: 1px; height: 160px;
    background: var(--divider);
  }
  .details { position: absolute; left: 306px; top: 86px; right: 24px; }
  .details__name { font-size: 34px; font-weight: 900; color: var(--navy); letter-spacing: -0.5px; line-height: 1.1; }
  .details__role { font-size: 19px; color: var(--khaki); margin-top: 4px; }
  .contacts { list-style: none; margin-top: 20px; }
  .contacts__item {
    display: flex; align-items: center; gap: 10px;
    font-size: 15px; color: var(--khaki); margin-bottom: 9px; white-space: nowrap;
  }
  .contacts__icon { width: 15px; height: 15px; flex: none; }
  /* Back */
  .card--back { background: var(--navy-deep); display: flex; align-items: center; justify-content: center; }
  .card--back .brand { gap: 14px; }
  .card--back .brand__mark { background: var(--white); width: 18px; height: 18px; }
  .card--back .brand__name { color: var(--white); font-size: 30px; }
</style>
</head>
<body>
<main class="canvas">
  <section class="card card--front" aria-label="Business card front">
    <div class="brand">
      <span class="brand__mark"></span>
      <span class="brand__name">Prairie Ridge Builders LLC</span>
    </div>
    <p class="address">287 N. Marbury El Paso Tx 79925</p>
    <span class="divider"></span>
    <div class="details">
      <h1 class="details__name">Tomas Verdugo</h1>
      <p class="details__role">Owner</p>
      <ul class="contacts">
        <li class="contacts__item">
          <svg class="contacts__icon" viewBox="0 0 16 16" aria-hidden="true"><path fill="#111448" d="M3.5 1 6 3.8 4.7 5.6c.8 1.9 2.2 3.3 4.1 4.1l1.8-1.3L13.4 11l-1.6 2.6C6.6 13.2 2.8 9.4 2.4 4.2Z"/></svg>
          9156820374
        </li>
        <li class="contacts__item">
          <svg class="contacts__icon" viewBox="0 0 16 16" aria-hidden="true"><rect x="1" y="3" width="14" height="10" fill="#111448"/><path d="M1 3l7 6 7-6" fill="none" stroke="#fff" stroke-width="1.2"/></svg>
          prairie.r.builders@mailhaven.net
        </li>
        <li class="contacts__item">
          <svg class="contacts__icon" viewBox="0 0 16 16" aria-hidden="true"><g fill="none" stroke="#111448" stroke-width="1.3"><circle cx="8" cy="8" r="6.5"/><ellipse cx="8" cy="8" rx="3" ry="6.5"/><path d="M1.5 8h13M2.6 4.8h10.8M2.6 11.2h10.8"/></g></svg>
          Commercial &amp; Residential
        </li>
      </ul>
    </div>
  </section>

  <section class="card card--back" aria-label="Business card back">
    <div class="brand">
      <span class="brand__mark"></span>
      <span class="brand__name">Prairie Ridge Builders</span>
    </div>
  </section>
</main>
</body>
</html>
```